Bref créative
Hidden Meadows Stationary
Business Card, Letterhead, Envelope, Compliment Slip
Simple
Emre Karabulut
Mr
47 Foxglove Road,
Ilford,
Essex,
RM4 8TN
emre@hddnmdws.com
www.hddnmdws.com
Vat No: 472 8610 35
Vat No to be used in letterhead.
Logo, Maybe even a part of the logo....We're open to ideas.
HM Logo (If any other format is needed please let us know.

```html
<!DOCTYPE html>
<html lang="en">
<head>
<meta charset="utf-8">
<title>Hidden Meadows Stationary</title>
<link href="https://fonts.googleapis.com/css2?family=Questrial&display=swap" rel="stylesheet">
<style>
  :root {
    --backdrop: #a8a8a8;
    --paper: #ffffff;
    --card-grey: #8f8f8f;
    --ink: #5a5b5d;
    --ink-light: #9a9a9a;
    --green: #5cb848;
    --green-dark: #3f9a33;
    --rule: #d9d9d9;
  }
  * { margin: 0; padding: 0; box-sizing: border-box; }
  html, body { width: 1200px; height: 655px; overflow: hidden; }
  body {
    background: var(--backdrop);
    font-family: "Questrial", "Century Gothic", sans-serif;
    color: var(--ink);
    position: relative;
  }
  .sheet {
    position: absolute;
    background: var(--paper);
    box-shadow: 0 1px 3px rgba(0,0,0,0.25);
    overflow: hidden;
  }

  /* Company name */
  .brand {
    display: flex;
    justify-content: center;
    align-items: center;
    gap: 7px;
    white-space: nowrap;
  }
  .brand-square { width: 8px; height: 8px; background: var(--green); }
  .brand-name { color: var(--ink); letter-spacing: 0.5px; }

  .green-band {
    position: absolute;
    left: 0; right: 0; bottom: 0;
    background: linear-gradient(var(--green), var(--green-dark));
    color: #fff;
    display: flex;
    flex-direction: column;
    justify-content: center;
    align-items: center;
    text-align: center;
    gap: 3px;
    white-space: nowrap;
  }
  .band-details { font-size: 6px; letter-spacing: 0.2px; }
  .band-web { font-size: 6px; font-weight: bold; }

  /* Letterhead */
  .letterhead { left: 197px; top: 12px; width: 452px; height: 629px; }
  .letterhead .brand { position: absolute; top: 52px; left: 0; right: 0; }
  .letterhead .brand-name { font-size: 18px; }
  .letterhead .top-rule {
    position: absolute; top: 108px; left: 0; right: 0;
    height: 1px; background: var(--rule);
  }
  .letterhead .bottom-rule {
    position: absolute; bottom: 44px; left: 0; right: 0;
    height: 1px; background: var(--rule);
  }
  .letterhead .green-band { height: 40px; }

  /* Business card */
  .card-back {
    left: 24px; top: 355px; width: 163px; height: 132px;
    background: var(--card-grey);
  }
  .card-back .card-web {
    position: absolute; left: 22px; top: 88px;
    font-size: 7px; color: #fff;
  }
  .card-front { left: 24px; top: 487px; width: 163px; height: 137px; }
  .card-front .brand { position: absolute; top: 30px; left: 0; right: 0; gap: 5px; }
  .card-front .brand-name { font-size: 12px; }
  .card-front .brand-square { width: 6px; height: 6px; }
  .card-front .person {
    position: absolute; top: 70px; left: 0; right: 0; text-align: center;
  }
  .person-name { font-size: 8px; color: var(--ink); }
  .person-title { font-size: 5px; color: var(--ink-light); margin-top: 2px; }
  .card-front .green-band { height: 19px; }
  .card-front .band-details { font-size: 4px; letter-spacing: 0; }

  /* Envelope back */
  .envelope-back { left: 660px; top: 84px; width: 521px; height: 235px; }
  .envelope-back svg { position: absolute; inset: 0; }

  /* Envelope front */
  .envelope-front { left: 660px; top: 343px; width: 521px; height: 300px; }
  .envelope-front .brand { position: absolute; top: 52px; left: 0; right: 0; }
  .envelope-front .brand-name { font-size: 20px; }
  .envelope-front .bottom-rule {
    position: absolute; bottom: 58px; left: 0; right: 0;
    height: 1px; background: var(--rule);
  }
  .envelope-front .green-band { height: 42px; bottom: 14px; }
</style>
</head>
<body>

  <section class="sheet letterhead">
    <div class="brand">
      <span class="brand-square"></span>
      <span class="brand-name">Hidden Meadows</span>
    </div>
    <div class="top-rule"></div>
    <div class="bottom-rule"></div>
    <footer class="green-band">
      <span class="band-details">47 Foxglove Road, Ilford, Essex, RM4 8TN &nbsp;&bull;&nbsp; Vat No: 472 8610 35 &nbsp;&bull;&nbsp; emre@hddnmdws.com</span>
      <span class="band-web">www.hddnmdws.com</span>
    </footer>
  </section>

  <section class="sheet card-back">
    <span class="card-web">www.hddnmdws.com</span>
  </section>

  <section class="sheet card-front">
    <div class="brand">
      <span class="brand-square"></span>
      <span class="brand-name">Hidden Meadows</span>
    </div>
    <div class="person">
      <div class="person-name">Emre Karabulut</div>
      <div class="person-title">Director</div>
    </div>
    <footer class="green-band">
      <span class="band-details">47 Foxglove Road, Ilford, Essex, RM4 8TN &bull; emre@hddnmdws.com</span>
    </footer>
  </section>

  <section class="sheet envelope-back">
    <svg width="521" height="235" viewBox="0 0 521 235">
      <path d="M0 2 L200 88 Q260 100 320 88 L521 2" fill="none" stroke="#c9c9c9" stroke-width="1.2"/>
    </svg>
  </section>

  <section class="sheet envelope-front">
    <div class="brand">
      <span class="brand-square"></span>
      <span class="brand-name">Hidden Meadows</span>
    </div>
    <div class="bottom-rule"></div>
    <footer class="green-band">
      <span class="band-details">47 Foxglove Road, Ilford, Essex, RM4 8TN &nbsp;&bull;&nbsp; Vat No: 472 8610 35 &nbsp;&bull;&nbsp; emre@hddnmdws.com</span>
      <span class="band-web">www.hddnmdws.com</span>
    </footer>
  </section>

</body>
</html>
```